Church Website with Home Page and Member Sermon Library

I am in need of an updated design for our church website. This will include 4 pages (outlined below). We are a conservative, evangelical, Christian church. The site should be modern and clean, while still reflecting our conservative values. I already have a logo for our church, and I want the site to incorporate the logo, and match the logo/branding. Stock photos are allowed if needed, but I have uploaded some images of our church and would prefer those images to be used if possible. Any stock photos used should not include any people in the photos (scenery, nature, buildings, animals, etc. are fine).

The site will need 4 pages: Home, Support Us (Donate), Login, and Recording Library.

Page 1: Home
The home page should include the following sections:

- Navigation: Should include links to each section of the home page plus a "listen live" link which will take the user to a live-streaming site and a "support us" link which will take the user to a support/donate page.

- Announcements: Can be either a banner or some other design, but there needs to be some way for us to post announcements for visitors to see. I'm open for creative ideas in this section, but would like it not to take up a lot of room on the page.

- About Us: Should include address, service times (see attached document), and information about the church.

- Pastor Bio: A section that introduces our pastor and gives a short bio about our pastor. Would like this section to include a picture of our pastor. Somewhere in this section I would like to include this Bible reference: "And I will give you pastors according to mine heart, which shall feed you with knowledge and understanding. Jer 3:15 KJV"

- Articles of Faith (What We Believe): This should include several sub-sections each with a heading, body, and possibly 1 or more scripture references. I have attached a document to the brief that includes our articles of faith. Feel free to be creative with this section in how you lay these out and format them.

- Support Us: A small section that explains what kind of support someone can give and a link to a donation page. The link can say something like "Support Us" or "Donate Now".

- Contact form: A contact form that allows the visitor to send us a message. The contact form should ask for name, email, phone, and message.

- Footer: A footer that will be displayed on all pages of the site. This should include at a minimum a link to the home page (or a link to each individual section in the home page if you prefer), a link to "listen live", a link to "support us", a link to "contact us" (or you can put the contact form directly in the footer if you prefer), the address, and a "member login" link.

Page 2: Support Us
The donation page should include a form the visitor can fill out to make a donation. We will embed a third party form later. For this design, please just mock out the design with a basic form asking for name, phone, and email.

Page 3: Login
The recording library (detailed below) will require members to login with a shared numeric code before accessing the page. We need a design for a login screen. The screen should include navigation/footer just like all other pages, but the body of the login page will consist only of a form that asks the user to enter the access code and then a "login" button.

Page 4: Recording Library

The library page is a member-only page that will require a shared, numeric pass code to access. On this page, members will be able to access a filterable list of past sermons. The page by default should display most recent sermons, but should also include a search form that allows the member to filter the sermon list to find a particular sermon. The search form should allow the user to select a filter type (e.g. Speaker name, date, event, etc.) and type in a value to search. They should be able to add multiple filters and remove filters that have been added. Each sermon that is displayed in the result list should include basic information such as title, date, speaker, tags, etc. along with a download icon, and an embedded audio player where they can click a play button to stream it on-demand. Each sermon should also have clickable tags associated with it that can be used to find related sermons.
Updates

I have uploaded several images of our church. Feel free to incorporate these into your design if possible.

Target Market(s)

Church Members

Industry/Entity Type

Religion

Number of Pages Required

4 page

Font styles to use
Sans Serif

Colors

Designer to choose colors to be used in the design.

Requirements
Must have
• Must incorporate the logo (attached)
Nice to have
• Would like the design to incorporate pictures of our church (attached) instead of stock photos if possible.
Should not have
• Please avoid an overly cluttered design. Stock photos used should not include any people in the photos.

```html
<!DOCTYPE html>
<html lang="en">
<head>
<meta charset="utf-8">
<title>Library – Cedar Hill Chapel</title>
<link rel="stylesheet" href="https://fonts.googleapis.com/css2?family=Cinzel:wght@400;500;700&family=Montserrat:wght@400;500;600&display=swap">
<style>
:root{
  --green:#86a86d;
  --ink:#1d1d1d;
  --text:#555555;
  --muted:#9a9a9a;
  --line:#dedede;
  --footer:#2c2c2c;
  --footer-line:#8a8a8a;
  --white:#ffffff;
}
*{box-sizing:border-box;margin:0;padding:0}
html,body{width:1200px;height:2318px;overflow:hidden}
body{background:var(--white);font-family:'Montserrat',sans-serif;color:var(--ink);position:relative}
a{color:inherit;text-decoration:none}

/* header */
.site-header{position:absolute;top:0;left:0;width:1200px;height:140px;z-index:2}
.brand{position:absolute;left:140px;top:88px;display:flex;align-items:center;gap:8px;font-family:'Cinzel',serif;font-size:20px;color:var(--green);font-weight:400;letter-spacing:1px}
.brand-mark{width:12px;height:12px;background:var(--green);flex:none}
.main-nav{position:absolute;left:527px;top:50px;display:flex;font-size:14px;font-weight:500;color:#222}
.main-nav a{margin-right:35px}
.btn{display:inline-flex;align-items:center;justify-content:center;font-family:'Cinzel',serif;font-size:15px;color:var(--white);background:var(--green)}
.site-header .btn{position:absolute;left:930px;top:41px;width:98px;height:37px}

/* hero */
.hero{position:absolute;top:0;left:0;width:1200px;height:454px;
  background:linear-gradient(180deg,rgba(255,255,255,.95) 0%,rgba(255,255,255,.55) 18%,rgba(255,255,255,0) 40%),
  linear-gradient(100deg,#c9936a 0%,#e3bc98 30%,#c79064 55%,#b3784c 75%,#8a6a55 100%)}
.hero-title{position:absolute;top:240px;left:0;width:1200px;text-align:center;font-family:'Cinzel',serif;font-weight:400;font-size:58px;letter-spacing:5px;color:#111;line-height:1}
.hero-rule{position:absolute;left:519px;top:317px;width:162px;height:3px;background:#111}
.hero-rule-thin{position:absolute;left:560px;top:323px;width:79px;height:1px;background:#111}

/* library */
.library{position:absolute;top:489px;left:173px;width:856px}
.library-head{display:flex;align-items:center;height:52px;position:relative}
.library-head h2{font-family:'Cinzel',serif;font-weight:400;font-size:17px;letter-spacing:1.5px;width:305px;padding-left:1px;margin-top:12px}
.search{display:flex;height:52px;border:1px solid var(--line);width:550px}
.search-field{flex:1;display:flex;align-items:center;gap:10px;padding-left:21px;font-size:13px;color:#b3b3b3}
.search-filter{width:206px;background:var(--green);color:var(--white);font-size:15px;font-weight:600;display:flex;align-items:center;justify-content:space-between;padding:0 18px 0 19px;margin:-1px -1px -1px 0}
.head-divider{height:1px;background:var(--line);margin-top:12px}

.sermon-grid{display:grid;grid-template-columns:416px 416px;column-gap:22px;margin-top:39px}
.sermon{height:490px}
.sermon-row-rule{grid-column:1/-1;display:grid;grid-template-columns:416px 416px;column-gap:28px;margin:-1px 0 28px}
.sermon-row-rule span{height:1px;background:var(--line)}
.sermon-media{position:relative;width:416px;height:258px;background:linear-gradient(180deg,#a9a69a 0%,#7a8b72 45%,#3f5a46 80%,#304a39 100%)}
.play{position:absolute;left:169px;top:90px;width:78px;height:78px;border-radius:50%;background:rgba(255,255,255,.4);border:2px solid rgba(255,255,255,.85);display:flex;align-items:center;justify-content:center}
.sermon-date{margin-top:14px;height:16px;font-size:13px;display:flex;align-items:center;gap:6px;padding-left:3px}
.sermon-title{margin-top:9px;font-family:'Cinzel',serif;font-weight:700;font-size:19px;letter-spacing:1.6px;line-height:22px;padding-left:2px}
.sermon-desc{margin-top:6px;font-size:13.2px;line-height:21.6px;color:var(--text);padding-left:3px;height:65px}
.byline{margin-top:14px;height:24px;display:flex;align-items:center;font-size:13.5px;padding-left:3px}
.avatar{width:24px;height:24px;border-radius:50%;background:#a58c7a;margin-right:10px}
.byline .label{margin-right:5px}
.download{margin-left:auto;display:flex;align-items:center;gap:10px;font-size:13.5px}
.tags-label{margin-top:8px;line-height:18px;font-size:13px;padding-left:2px}
.accent .byline .label,.accent .tags-label{color:var(--green)}
.tag-list{margin-top:10px;display:flex;gap:7px;flex-wrap:wrap}
.tag{height:26px;padding:0 12px;border:1px solid var(--line);border-radius:14px;font-size:12.5px;letter-spacing:1px;display:inline-flex;align-items:center;color:#333}
.tag-list .tag + .tag + .tag{margin-left:8px}

/* related tags */
.related{position:absolute;top:1698px;left:173px;width:856px;border-top:1px solid var(--line)}
.related h2{font-family:'Cinzel',serif;font-weight:400;font-size:17px;letter-spacing:1.5px;margin-top:31px;padding-left:2px}
.related-tags{margin-top:17px;display:flex;flex-wrap:wrap;gap:14px 10px;padding-left:1px}
.related-tags .tag{height:32px;padding:0 15px;border-radius:17px;font-size:13.5px;letter-spacing:1.1px}

/* footer */
.site-footer{position:absolute;top:1890px;left:0;width:1200px;height:428px;background:var(--footer);color:#d8d8d8}
.footer-brand{position:absolute;left:150px;top:172px;width:300px;display:flex;align-items:center;justify-content:center;gap:10px;font-family:'Cinzel',serif;font-size:20px;color:var(--green);letter-spacing:1px;white-space:nowrap}
.footer-brand .brand-mark{width:14px;height:14px}
.contact{position:absolute;left:477px;top:56px;width:551px}
.contact h2{font-family:'Cinzel',serif;font-weight:400;font-size:19px;letter-spacing:2px;color:#e6e6e6}
.contact-form{position:relative;margin-top:26px;height:150px}
.field{position:absolute;height:24px;border-bottom:1px solid var(--footer-line);font-size:12px;color:#cfcfcf;display:flex;align-items:flex-start;justify-content:space-between;padding-top:2px}
.field.name{left:0;top:0;width:252px}
.field.phone{left:0;top:44px;width:252px}
.field.email{left:0;top:88px;width:252px}
.field.message{left:281px;top:0;width:270px;height:112px}
.send{position:absolute;left:477px;top:247px;width:109px;height:36px;border:1px solid var(--green);color:var(--green);font-family:'Cinzel',serif;font-size:14px;display:flex;align-items:center;justify-content:center;gap:8px}
.footer-note{position:absolute;left:477px;top:314px;font-size:12px;color:#d0d0d0}
.site-footer .btn{position:absolute;left:927px;top:303px;width:99px;height:37px}
.copyright{position:absolute;left:186px;top:386px;font-size:12px;color:#e0e0e0}
.social{position:absolute;left:926px;top:388px;display:flex;gap:16px}
.social span{width:11px;height:11px;border-radius:50%;background:#e6e6e6}
</style>
</head>
<body>

<section class="hero" role="img" aria-label="Photo of wooden church pews inside the sanctuary">
  <h1 class="hero-title">LIBRARY</h1>
  <div class="hero-rule"></div>
  <div class="hero-rule-thin"></div>
</section>

<header class="site-header">
  <a class="brand" href="#"><span class="brand-mark"></span>Cedar Hill Chapel</a>
  <nav class="main-nav">
    <a href="#">Home</a><a href="#">About</a><a href="#">Our Pastor</a><a href="#">Articles Of Faith</a>
  </nav>
  <a class="btn" href="#">DONATE</a>
</header>

<main class="library">
  <div class="library-head">
    <h2>LIST OF PAST SERMONS</h2>
    <form class="search">
      <div class="search-field">
        <svg width="16" height="16" viewBox="0 0 16 16" fill="none" stroke="#b0b0b0" stroke-width="1.6"><circle cx="6.5" cy="6.5" r="5"/><path d="M10.2 10.2L15 15"/></svg>
        Type your request here
      </div>
      <div class="search-filter">Search by speaker
        <svg width="10" height="6" viewBox="0 0 10 6"><path d="M0 0h10L5 6z" fill="#fff"/></svg>
      </div>
    </form>
  </div>
  <div class="head-divider"></div>

  <div class="sermon-grid">
    <article class="sermon">
      <div class="sermon-media" role="img" aria-label="Sermon video still of the speaker at the pulpit">
        <div class="play"><svg width="18" height="20" viewBox="0 0 18 20"><path d="M0 0l18 10L0 20z" fill="#86a86d"/></svg></div>
      </div>
      <div class="sermon-date"><svg width="11" height="11" viewBox="0 0 11 11" fill="none" stroke="#222" stroke-width="1.2"><rect x="1" y="2" width="9" height="8"/><path d="M1 4.5h9M3.5 0.5v2M7.5 0.5v2"/></svg>Fab 12, 2023</div>
      <h3 class="sermon-title">ULLAMCORPER FACILISI EGESTAS</h3>
      <p class="sermon-desc">Ut diam tortor consectetur lacus scelerisque tortor congue viverra egestas. Tristique in consectetur leo arcu blandit diam et sed volutpat.</p>
      <div class="byline"><span class="avatar"></span><span class="label">by:</span>Marian Keller
        <a class="download" href="#">Download <svg width="16" height="16" viewBox="0 0 16 16" fill="none" stroke="#86a86d" stroke-width="1.6"><path d="M8 1v10M4 7l4 4 4-4M1 12v3h14v-3"/></svg></a></div>
      <p class="tags-label">search tags:</p>
      <div class="tag-list"><a class="tag" href="#">Ullamcorper facilis</a><a class="tag" href="#">facilis</a><a class="tag" href="#">Ullamcorper</a></div>
    </article>
    <article class="sermon accent">
      <div class="sermon-media" role="img" aria-label="Sermon video still of the speaker at the pulpit">
        <div class="play"><svg width="18" height="20" viewBox="0 0 18 20"><path d="M0 0l18 10L0 20z" fill="#86a86d"/></svg></div>
      </div>
      <div class="sermon-date"><svg width="11" height="11" viewBox="0 0 11 11" fill="none" stroke="#222" stroke-width="1.2"><rect x="1" y="2" width="9" height="8"/><path d="M1 4.5h9M3.5 0.5v2M7.5 0.5v2"/></svg>Fab 12, 2023</div>
      <h3 class="sermon-title">ULLAMCORPER FACILISI EGESTAS</h3>
      <p class="sermon-desc">Ut diam tortor consectetur lacus scelerisque tortor congue viverra egestas. Tristique in consectetur leo arcu blandit diam et sed volutpat.</p>
      <div class="byline"><span class="avatar"></span><span class="label">by:</span>Marian Keller
        <a class="download" href="#">Download <svg width="16" height="16" viewBox="0 0 16 16" fill="none" stroke="#86a86d" stroke-width="1.6"><path d="M8 1v10M4 7l4 4 4-4M1 12v3h14v-3"/></svg></a></div>
      <p class="tags-label">search tags:</p>
      <div class="tag-list"><a class="tag" href="#">Ullamcorper facilis</a><a class="tag" href="#">facilis</a><a class="tag" href="#">Ullamcorper</a></div>
    </article>

    <div class="sermon-row-rule"><span></span><span></span></div>

    <article class="sermon">
      <div class="sermon-media" role="img" aria-label="Sermon video still of the speaker at the pulpit">
        <div class="play"><svg width="18" height="20" viewBox="0 0 18 20"><path d="M0 0l18 10L0 20z" fill="#86a86d"/></svg></div>
      </div>
      <div class="sermon-date"><svg width="11" height="11" viewBox="0 0 11 11" fill="none" stroke="#222" stroke-width="1.2"><rect x="1" y="2" width="9" height="8"/><path d="M1 4.5h9M3.5 0.5v2M7.5 0.5v2"/></svg>Fab 12, 2023</div>
      <h3 class="sermon-title">ULLAMCORPER FACILISI EGESTAS</h3>
      <p class="sermon-desc">Ut diam tortor consectetur lacus scelerisque tortor congue viverra egestas. Tristique in consectetur leo arcu blandit diam et sed volutpat.</p>
      <div class="byline"><span class="avatar"></span><span class="label">by:</span>Marian Keller
        <a class="download" href="#">Download <svg width="16" height="16" viewBox="0 0 16 16" fill="none" stroke="#86a86d" stroke-width="1.6"><path d="M8 1v10M4 7l4 4 4-4M1 12v3h14v-3"/></svg></a></div>
      <p class="tags-label">search tags:</p>
      <div class="tag-list"><a class="tag" href="#">Ullamcorper facilis</a><a class="tag" href="#">facilis</a><a class="tag" href="#">Ullamcorper</a></div>
    </article>
    <article class="sermon accent">
      <div class="sermon-media" role="img" aria-label="Sermon video still of the speaker at the pulpit">
        <div class="play"><svg width="18" height="20" viewBox="0 0 18 20"><path d="M0 0l18 10L0 20z" fill="#86a86d"/></svg></div>
      </div>
      <div class="sermon-date"><svg width="11" height="11" viewBox="0 0 11 11" fill="none" stroke="#222" stroke-width="1.2"><rect x="1" y="2" width="9" height="8"/><path d="M1 4.5h9M3.5 0.5v2M7.5 0.5v2"/></svg>Fab 12, 2023</div>
      <h3 class="sermon-title">ULLAMCORPER FACILISI EGESTAS</h3>
      <p class="sermon-desc">Ut diam tortor consectetur lacus scelerisque tortor congue viverra egestas. Tristique in consectetur leo arcu blandit diam et sed volutpat.</p>
      <div class="byline"><span class="avatar"></span><span class="label">by:</span>Marian Keller
        <a class="download" href="#">Download <svg width="16" height="16" viewBox="0 0 16 16" fill="none" stroke="#86a86d" stroke-width="1.6"><path d="M8 1v10M4 7l4 4 4-4M1 12v3h14v-3"/></svg></a></div>
      <p class="tags-label">search tags:</p>
      <div class="tag-list"><a class="tag" href="#">Ullamcorper facilis</a><a class="tag" href="#">facilis</a><a class="tag" href="#">Ullamcorper</a></div>
    </article>
  </div>
</main>

<section class="related">
  <h2>RELATED SERMONS TAGS</h2>
  <div class="related-tags">
    <a class="tag" href="#">Ullamcorper facilis</a>
    <a class="tag" href="#">eu id tempo</a>
    <a class="tag" href="#">in consectetur leo</a>
    <a class="tag" href="#">elementum gravida</a>
    <a class="tag" href="#">entum gravida</a>
    <a class="tag" href="#">in consectetur leo</a>
    <a class="tag" href="#">elementum gravida</a>
    <a class="tag" href="#">entum gravida</a>
  </div>
</section>

<footer class="site-footer">
  <div class="footer-brand"><span class="brand-mark"></span>Cedar Hill Chapel</div>
  <section class="contact">
    <h2>CONTACT US</h2>
    <form class="contact-form">
      <label class="field name">Full Name:<svg width="11" height="12" viewBox="0 0 11 12" fill="none" stroke="#d0d0d0" stroke-width="1.1"><circle cx="5.5" cy="3.5" r="2.7"/><path d="M1 11.5c0-3 2-4.5 4.5-4.5S10 8.5 10 11.5"/></svg></label>
      <label class="field phone">Phone:<svg width="12" height="12" viewBox="0 0 12 12" fill="none" stroke="#d0d0d0" stroke-width="1.1"><path d="M2 1h2.5l1 3-1.5 1a6 6 0 0 0 3 3l1-1.5 3 1V10a1 1 0 0 1-1 1A9.5 9.5 0 0 1 1 2a1 1 0 0 1 1-1z"/></svg></label>
      <label class="field email">Email Address:<svg width="13" height="10" viewBox="0 0 13 10" fill="none" stroke="#d0d0d0" stroke-width="1.1"><rect x="0.6" y="0.6" width="11.8" height="8.8"/><path d="M0.6 0.6l5.9 5 5.9-5"/></svg></label>
      <label class="field message">Message<svg width="13" height="13" viewBox="0 0 13 13" fill="none" stroke="#d0d0d0" stroke-width="1.1"><path d="M9 1.5l2.5 2.5L4 11.5H1.5V9z M1 12.5h11"/></svg></label>
    </form>
  </section>
  <a class="send" href="#">SEND US <svg width="18" height="8" viewBox="0 0 18 8" fill="none" stroke="#86a86d" stroke-width="1.2"><path d="M0 4h17M13 1l4 3-4 3"/></svg></a>
  <p class="footer-note">Aliquam at commodo venenatis quis. Velit neque interdum molestie risus.</p>
  <a class="btn" href="#">DONATE</a>
  <p class="copyright">Copyright 2023 Cedar Hill Chapel I All rights reserved</p>
  <div class="social" aria-label="Social links"><span></span><span></span><span></span><span></span></div>
</footer>

</body>
</html>
```